Summer children's holiday club

Hi i need a flyer design for a children's holiday club for the summer.24th July-3rd September 2015.

Bright Pebbles holiday club runs every school holiday for children aged 3 to 11 years (only closing on public bank holidays). The activity day runs from 8.00am to 6.00pm, with the option to book a shorter day from 8.00am to 1.00pm or 1.00pm-6.00pm.

The focus for Bright Pebbles holiday club is about having as much FUN as possible!

With a huge programme of activities on offer, including everything from Parachute Play, Role Play, Golf and Relay Races in our large hall,Den Making, Trips to the park, Themed days, Painting and Sensory Sessions in our 'Calm Nook Corner', there are a huge variety of activities on offer to suit both the sporty and more creative child.

Our programme of activities changes daily, even throughout the long summer holiday, and with a team of highly qualified and suitably trained staff, we are fully confident your child will always have a time to remember at Bright Pebbles holiday club.

Our holiday club is registered with Nurturemark.

Fees

Holiday Club 8am-6pm £25.00 (includes all meals)
8am-1pm or 1pm-6pm £15.00 (includes AM or PM snacks)
The choice of water or milk provided throughout the day.

Discounts Available
Book the first child and the second child gets 5% discount. Children must be siblings and attend identical sessions to qualify.

Receive a further 5% discount for siblings on booking a full week. Please note a full week is considered to mean bookings made for Monday through to Friday 8.00am-6.00pm.

(Maximum discount of 10%)

Our normal marketing design is a printmoor one( with children playing on a trampoline) so i would still like to use that if possible. We have already got the brochure that's on the website that i use for our afterschool club, so i need something designed a little different for the holiday club.

Target Market(s)

Parents with young children 3-11years old

Industry/Entity Type

Childcare

Requirements
Must have
• The design needs to be bright and communicate that we offer discount, provide a hot lunch, breakfast and afternoon snack in the price. Prices,address,phone number and dates will also need to be included on it.

```html
<!DOCTYPE html>
<html lang="en">
<head>
<meta charset="utf-8">
<title>Bright Pebbles Holiday Club – Summer Flyer</title>
<link rel="stylesheet" href="https://fonts.googleapis.com/css2?family=Baloo+2:wght@500;600&family=Comic+Neue:wght@400;700&family=Open+Sans:wght@400;700&family=Patrick+Hand&display=swap">
<style>
  :root{
    --stage:#1b1b1b;
    --paper:#ffffff;
    --sky-top:#7fc6ee;
    --sky-mid:#a9daf5;
    --sky-low:#dcf0fb;
    --ink-blue:#1f5fa8;
    --deep-blue:#1d4f9a;
    --golf:#d9262b;
    --trips:#1e63b4;
    --relay:#c6b12a;
    --roleplay:#3f8a2e;
    --parachute:#c0202a;
    --price-red:#c0202a;
    --max-green:#3aa52a;
    --badge-blue:#2a8fd6;
  }
  *{box-sizing:border-box;margin:0;padding:0}
  html,body{width:1200px;height:1200px;overflow:hidden;background:var(--stage)}
  body{position:relative;font-family:"Comic Neue",cursive}

  .flyer{position:absolute;left:208px;width:794px;background:var(--paper)}
  .flyer--front{top:29px;height:552px}
  .flyer--back{top:614px;height:558px}
  .flyer__face{position:absolute;left:11px;top:9px;width:772px;overflow:hidden}
  .flyer--front .flyer__face{height:533px;background:linear-gradient(180deg,var(--sky-top) 0%,var(--sky-mid) 55%,var(--sky-low) 80%)}
  .flyer--back .flyer__face{top:10px;height:538px;background:linear-gradient(180deg,var(--sky-top) 0%,var(--sky-low) 22%,#fff 38%,#fff 100%)}

  .abs{position:absolute}

  .title{left:0;width:772px;top:34px;text-align:center;font-family:"Baloo 2",cursive;font-weight:500;font-size:53px;color:var(--ink-blue);line-height:1}
  .dates{left:0;width:772px;top:96px;text-align:center;font-family:"Open Sans",sans-serif;font-size:28px;color:#fff;letter-spacing:-.3px}
  .dates b{font-weight:700}

  .cloud{background:#fff;border-radius:50%;opacity:.9}
  .sun{background:radial-gradient(circle at 40% 40%,#ffe24a,#f5c400);border-radius:50%}

  .hero{border-radius:50%;background:radial-gradient(circle,#5aa5e0 0%,#2f7ccc 70%,#1f5fb0 100%)}

  .ages{left:56px;top:190px;font-family:"Comic Neue",cursive;font-weight:700;font-size:23px;line-height:29.4px;color:var(--ink-blue);text-transform:uppercase}

  .activity{font-family:"Comic Neue",cursive;font-weight:700;font-size:19px;line-height:1}
  .activity--golf{left:530px;top:194px;color:var(--golf)}
  .activity--trips{left:572px;top:228px;color:var(--trips)}
  .activity--relay{left:540px;top:275px;color:var(--relay)}
  .activity--role{left:619px;top:325px;color:var(--roleplay)}
  .activity--parachute{left:529px;top:364px;color:var(--parachute)}

  .ground{left:0;width:772px}
  .contact__phone{display:flex;align-items:center;gap:10px;font-family:"Open Sans",sans-serif;color:#fff;line-height:1}
  .phone-icon{width:38px;height:34px;border-radius:7px;background:linear-gradient(180deg,#7fd35b,#3f9e2a);display:flex;align-items:center;justify-content:center;box-shadow:0 1px 2px rgba(0,0,0,.25)}
  .contact__address{font-family:"Comic Neue",cursive;font-weight:700;color:#fff;font-size:16.5px;line-height:21px}

  .hours{left:414px;top:436px;color:#fff;font-family:"Comic Neue",cursive;font-weight:700}
  .hours__label{font-size:22px;line-height:24px}
  .hours__line{font-size:21px;line-height:25px}

  .curl{right:0;bottom:0;width:110px;height:100px}
  .curl__text{right:10px;bottom:28px;width:100px;transform:rotate(-42deg);font-family:"Comic Neue",cursive;font-weight:700;font-size:14px;color:var(--ink-blue);text-align:center;line-height:15px}

  .intro{left:29px;top:26px;width:724px;font-family:"Comic Neue",cursive;font-size:13.4px;line-height:15px;color:var(--ink-blue)}
  .intro p+p{margin-top:15px}

  .section-label{font-family:"Comic Neue",cursive;font-weight:700;font-size:19px;color:var(--deep-blue);line-height:23px}
  .section-body{font-family:"Comic Neue",cursive;font-size:13.4px;line-height:17.5px;color:var(--ink-blue)}
  .price{color:var(--price-red);font-weight:700;font-size:15px}
  .section-body b{font-weight:700}
  .max{color:var(--max-green);font-weight:700;font-size:15px}

  .registered{left:26px;top:408px;font-family:"Patrick Hand",cursive;font-size:20px;color:#3f8fd6;letter-spacing:.5px}
  .regulator{left:338px;top:404px;display:flex;align-items:center;gap:6px;font-family:"Comic Neue",cursive;font-weight:700;font-size:15px;color:var(--badge-blue)}
  .regulator__mark{width:26px;height:26px;background:var(--badge-blue);border-radius:3px}
</style>
</head>
<body>

<section class="flyer flyer--front" aria-label="Flyer front">
  <div class="flyer__face">
    <h1 class="abs title">Bright Pebbles Holiday Club</h1>
    <p class="abs dates"><b>24TH</b> JULY - <b>3RD</b> SEPTEMBER 2015</p>

    <div class="abs cloud" role="img" aria-label="Drawn cloud" style="left:40px;top:110px;width:90px;height:30px"></div>
    <div class="abs sun" role="img" aria-label="Drawn sun" style="left:676px;top:110px;width:38px;height:38px"></div>
    <div class="abs cloud" role="img" aria-label="Drawn cloud" style="left:624px;top:130px;width:80px;height:30px"></div>

    <div class="abs hero" role="img" aria-label="Illustration of four children bouncing on a round trampoline" style="left:244px;top:157px;width:274px;height:274px"></div>

    <p class="abs ages">Place<br>available<br>for<br>children<br>aged<br>3 to 11 years</p>

    <span class="abs activity activity--golf">Golf</span>
    <span class="abs activity activity--trips">Trips to the park</span>
    <span class="abs activity activity--relay">Relay Races</span>
    <span class="abs activity activity--role">Role Play</span>
    <span class="abs activity activity--parachute">Parachute Play</span>

    <svg class="abs ground" style="top:398px" width="772" height="135" viewBox="0 0 772 135" aria-hidden="true">
      <defs>
        <linearGradient id="grassFront" x1="0" y1="0" x2="0" y2="1">
          <stop offset="0" stop-color="#7fcd58"/><stop offset="1" stop-color="#5cb83a"/>
        </linearGradient>
      </defs>
      <path d="M0 18 C120 0 230 30 380 24 C520 18 620 0 772 10 L772 135 L0 135 Z" fill="url(#grassFront)"/>
    </svg>

    <div class="abs contact__phone" style="left:54px;top:430px;font-size:37px">
      <span class="phone-icon"><svg width="22" height="22" viewBox="0 0 24 24" aria-hidden="true"><path fill="#fff" d="M6.6 10.8a15.1 15.1 0 0 0 6.6 6.6l2.2-2.2c.3-.3.7-.4 1-.2 1.1.4 2.3.6 3.6.6.6 0 1 .4 1 1V20c0 .6-.4 1-1 1A17 17 0 0 1 3 4c0-.6.4-1 1-1h3.5c.6 0 1 .4 1 1 0 1.3.2 2.5.6 3.6.1.3 0 .7-.2 1z"/></svg></span>
      07911482307
    </div>
    <p class="abs contact__address" style="left:56px;top:470px">Hollybank Lane Community Church<br>Larchwood Drive, Sale, Cheshire M33 9QX</p>

    <div class="abs hours">
      <p class="hours__label">OPEN</p>
      <p class="hours__line">Mon-Fri: 8:00am-6:00pm</p>
      <p class="hours__line">Sat &amp; Sun: Closed</p>
    </div>

    <svg class="abs curl" viewBox="0 0 110 100" aria-hidden="true">
      <defs>
        <linearGradient id="curlShade" x1="0" y1="0" x2="1" y2="1">
          <stop offset="0" stop-color="#ffffff"/><stop offset=".6" stop-color="#e6e9ec"/><stop offset="1" stop-color="#b9bec3"/>
        </linearGradient>
      </defs>
      <path d="M110 0 L110 100 L0 100 C30 80 70 40 110 0 Z" fill="url(#curlShade)"/>
    </svg>
    <p class="abs curl__text">Flip For<br>More Details</p>
  </div>
</section>

<section class="flyer flyer--back" aria-label="Flyer back">
  <div class="flyer__face">
    <div class="abs intro">
      <p>Bright Pebbles holiday club runs every school holiday for children aged 3 to 11 years (only closing on public bank holidays). The activity day runs from 8.00am to 6.00pm, with the option to book a shorter day from 8.00am to 1.00pm or 1.00pm-6.00pm.</p>
      <p>The focus for Bright Pebbles holiday club is about having as much FUN as possible! With a huge programme of activities on offer, including everything from Parachute Play, Role Play, Golf and Relay Races in our large hall, to our Dough Station, Trips to the park, Themed days, Painting and Sensory Sessions in our 'Calm Nook Corner', there are a huge variety of activities on offer to suit both the sporty and more creative child.</p>
      <p>Our programme of activities changes daily, even throughout the long summer holiday, and with a team of highly qualified and suitably trained staff, we are fully confident your child will always have a time to remember at Bright Pebbles holiday club.</p>
    </div>

    <h2 class="abs section-label" style="left:27px;top:245px">FEES</h2>
    <div class="abs section-body" style="left:164px;top:220px;width:600px">
      <p>(Please note holiday club prices do not apply to regular nursery users)</p>
      <p>Holiday Club 8am-6pm <span class="price">£25.00</span> (includes all meals)</p>
      <p>8am-1pm or 1pm-6pm <span class="price">£15.00</span> (includes AM or PM snacks)</p>
      <p>The choice of water or milk provided throughout the day.</p>
    </div>

    <h2 class="abs section-label" style="left:27px;top:310px;text-align:center">DISCOUNTS<br>AVAILABLE</h2>
    <div class="abs section-body" style="left:164px;top:301px;width:580px">
      <p>Book the first child and the second child gets <b>5% discount</b>. Children must be siblings and attend identical sessions to qualify.</p>
      <p>Receive a further <b>5% discount</b> for siblings on booking a full week. Please note a full week is considered to mean bookings made for Monday through to Friday 8.00am-6.00pm.</p>
      <p class="max">(MAXIMUM DISCOUNT OF 10%)</p>
    </div>

    <p class="abs registered">Our Holiday Club Is Registered With</p>
    <div class="abs regulator"><span class="regulator__mark"></span>Nurturemark</div>

    <svg class="abs ground" style="top:440px" width="772" height="98" viewBox="0 0 772 98" aria-hidden="true">
      <path d="M0 12 C140 0 260 22 400 18 C540 14 640 0 772 8 L772 98 L0 98 Z" fill="#6cc04a"/>
    </svg>

    <div class="abs hero" role="img" aria-label="Illustration of four children bouncing on a round trampoline" style="left:602px;top:391px;width:138px;height:138px"></div>

    <div class="abs contact__phone" style="left:30px;top:478px;font-size:31px">
      <span class="phone-icon"><svg width="22" height="22" viewBox="0 0 24 24" aria-hidden="true"><path fill="#fff" d="M6.6 10.8a15.1 15.1 0 0 0 6.6 6.6l2.2-2.2c.3-.3.7-.4 1-.2 1.1.4 2.3.6 3.6.6.6 0 1 .4 1 1V20c0 .6-.4 1-1 1A17 17 0 0 1 3 4c0-.6.4-1 1-1h3.5c.6 0 1 .4 1 1 0 1.3.2 2.5.6 3.6.1.3 0 .7-.2 1z"/></svg></span>
      07911482307
    </div>
    <p class="abs contact__address" style="left:292px;top:476px;width:316px;text-align:center;font-weight:400;font-size:16px">Hollybank Lane Community Church<br>Larchwood Drive, Sale, Cheshire M33 9QX</p>
  </div>
</section>

</body>
</html>
```